Professional website for psychological services

Create a professional, easy to navigate website using soothing coastal images and incorporate company logo in design. Website is for a small private clinic that provides psychological services and must be appealing to professional men and women. A website I really like is www.velmorlodge.example I would love something like similar.

Target Market(s)

Professional men and women seeking psychological services

Industry/Entity Type

Mental Health

Number of Pages Required

5+ page

Requirements
Must have
• The website must incorporate the logo provided. The name of the company/website is Brindle Oak Wellness Aftercare. Colors must compliment the logo, must be coastal and soothing yet very professional. I would like a website like www.velmorlodge.example
• Pages will be:Home, Services, FAQ and Contact Us. The images included of the building and office are for the contact us page. Under the tab Servies: Individual Psychotherapy, Family Therapy, EMDR I will provide specific content for each.
Nice to have
• I want the website to be easy to navigate and the font easy to read. The writing on the logo is very light and I'm open to changing it slightly if it will be better aesthetically.
Should not have
• Please no pictures of any swimsuits, alcoholic beverages, etc. This is a professional psychological clinic.

```html
<!DOCTYPE html>
<html lang="en">
<head>
<meta charset="utf-8">
<title>Brindle Oak Wellness Aftercare — Psychological Services</title>
<link rel="stylesheet" href="https://fonts.googleapis.com/css2?family=Old+Standard+TT:ital,wght@0,400;0,700;1,400&family=Dancing+Script:wght@700&family=Jost:wght@400&display=swap">
<style>
:root{
  --ink:#2b2b2b;
  --teal:#1ea7c6;
  --white:#ffffff;
  --sand:#e7d7c3;
  --peach-top:#fbefe6;
  --peach-mid:#f8e2d6;
  --sea-mist:#d3dcd6;
  --sea-gray:#c9d4d3;
  --footer:#1f2628;
  --footer-line:#55605f;
  --field:#fbfbfb;
}
*{box-sizing:border-box;margin:0;padding:0}
html,body{width:1200px;height:3114px;overflow:hidden}
body{font-family:"Old Standard TT",Georgia,serif;color:var(--ink);background:var(--white);position:relative}

.site-header{position:absolute;left:0;top:0;width:1200px;height:218px;background:var(--white)}
.brand{position:absolute;left:0;width:1200px;top:70px;text-align:center;font-size:46px;color:var(--teal)}
.brand-dot{display:inline-block;width:16px;height:16px;border-radius:50%;background:var(--teal);margin-right:12px;vertical-align:middle}
.main-nav{position:absolute;top:178px;left:0;width:1200px;text-align:center;font-size:16px;letter-spacing:.5px}
.main-nav a{color:var(--ink);text-decoration:none;padding:0 22px}
.main-nav .sep{color:var(--ink)}

.hero{position:absolute;top:218px;left:0;width:1200px;height:590px;
  background:linear-gradient(180deg,#3c4a4a 0%,#5c6a60 30%,#2f8f9a 55%,#35b6c4 70%,#b07a3b 88%,#8a5a2a 100%)}
.hero-band{position:absolute;left:0;top:212px;width:1200px;height:122px;background:rgba(20,24,24,.35)}
.hero-title{position:absolute;left:0;top:240px;width:1200px;text-align:center;font-size:50px;color:var(--white);font-weight:400}

.content{position:absolute;top:808px;left:0;width:1200px;height:2092px;
  background:linear-gradient(180deg,var(--peach-top) 0%,var(--peach-mid) 35%,#efe0d6 55%,var(--sea-mist) 72%,var(--sea-gray) 100%)}

.photo{position:absolute;border-radius:50%;border:6px solid rgba(255,255,255,.55)}
.btn{position:absolute;display:block;height:35px;border-radius:18px;background:var(--sand);
  font-family:"Dancing Script",cursive;font-size:17px;color:var(--ink);text-align:center;line-height:35px}

.about-photo{left:119px;top:108px;width:290px;height:290px;background:radial-gradient(circle at 50% 40%,#c9a48e 0%,#5a3e30 45%,#3f6b3a 75%,#2f4f2c 100%)}
.about-title{position:absolute;left:430px;top:130px;font-size:44px;font-weight:400}
.about-title .accent{color:var(--teal)}
.about-text{position:absolute;left:430px;top:212px;width:540px;font-size:13.5px;font-style:italic;line-height:1.4}
.about-text p+p{margin-top:18px}
.about-btn{left:430px;top:352px;width:125px}

.services-title{position:absolute;left:0;top:500px;width:1200px;text-align:center;font-size:44px;font-weight:400}

.service h3{position:absolute;font-size:22px;font-weight:400}
.service .desc{position:absolute;width:560px;font-size:13px;line-height:1.65}
.service ul{position:absolute;list-style:none;font-size:13px;line-height:1}
.service li{margin-bottom:12px;display:flex;align-items:center}
.service li svg{margin-right:6px;flex:none}

.svc-individual h3{left:143px;top:618px}
.svc-individual .desc{left:143px;top:652px}
.svc-individual ul{left:143px;top:706px}
.svc-individual .btn{left:143px;top:792px;width:124px}
.svc-individual .photo{left:754px;top:587px;width:286px;height:286px;background:radial-gradient(circle at 50% 50%,#d9b9a0 0%,#8b6b55 40%,#2d3438 75%,#e9e4e0 100%)}

.svc-family h3{left:489px;top:965px}
.svc-family .desc{left:489px;top:999px}
.svc-family ul{left:489px;top:1053px}
.svc-family .btn{left:489px;top:1138px;width:124px}
.svc-family .photo{left:158px;top:934px;width:286px;height:286px;background:radial-gradient(circle at 50% 45%,#c8a48a 0%,#7e6a5c 40%,#b7b0aa 70%,#e7ddd2 100%)}

.svc-emdr h3{left:143px;top:1320px}
.svc-emdr .desc{left:143px;top:1354px}
.svc-emdr ul{left:143px;top:1408px}
.svc-emdr .btn{left:143px;top:1494px;width:124px}
.svc-emdr .photo{left:754px;top:1281px;width:286px;height:286px;background:radial-gradient(circle at 40% 40%,#e3c2aa 0%,#a47f63 35%,#6f8e9a 65%,#dfe6ea 100%)}

.contact-title{position:absolute;left:0;top:1722px;width:1200px;text-align:center;font-size:28px;color:var(--white);letter-spacing:1px;font-weight:400}
.field{position:absolute;background:var(--field);border-radius:3px;font-family:"Jost",sans-serif;font-size:13px;color:#444;padding:12px 18px}
.f-first{left:344px;top:1775px;width:250px;height:41px}
.f-last{left:606px;top:1775px;width:250px;height:41px}
.f-phone{left:344px;top:1828px;width:250px;height:41px}
.f-email{left:606px;top:1828px;width:250px;height:41px}
.f-message{left:344px;top:1880px;width:512px;height:83px}
.submit-btn{left:538px;top:1987px;width:124px}

.site-footer{position:absolute;top:2900px;left:0;width:1200px;height:214px;
  background:linear-gradient(180deg,#3a4446 0%,#2a3234 45%,#5a5236 62%,#1c2223 100%)}
.footer-brand{position:absolute;left:140px;top:70px;font-size:36px;color:var(--teal)}
.footer-brand .brand-dot{width:12px;height:12px;margin-right:10px}
.follow{position:absolute;left:915px;top:52px;font-family:"Jost",sans-serif;font-size:22px;color:var(--white)}
.socials{position:absolute;left:898px;top:94px;display:flex;gap:4px}
.socials span{width:28px;height:28px;border-radius:50%;border:2px solid rgba(255,255,255,.8);display:block}
.socials .s1{background:#3b5a9a}.socials .s2{background:#2ca7e0}.socials .s3{background:#1d7fb5}.socials .s4{background:#d6332a}.socials .s5{background:#7a3b3b}
.footer-rule{position:absolute;left:140px;top:177px;width:920px;height:1px;background:var(--footer-line)}
.copyright{position:absolute;left:0;top:187px;width:1200px;text-align:center;font-family:"Jost",sans-serif;font-size:12px;color:var(--white)}
</style>
</head>
<body>

<header class="site-header">
  <div class="brand"><span class="brand-dot"></span>Brindle Oak</div>
  <nav class="main-nav">
    <a href="#">Home</a><span class="sep">|</span><a href="#">Services</a><span class="sep">|</span><a href="#">FAQs</a><span class="sep">|</span><a href="#">Contact Us.</a>
  </nav>
</header>

<section class="hero" role="img" aria-label="Coastal cove with a waterfall, turquoise water and golden cliffs">
  <div class="hero-band"></div>
  <h1 class="hero-title">We Provide Psychological Services.</h1>
</section>

<main class="content">
  <section class="about">
    <div class="photo about-photo" role="img" aria-label="Portrait of the clinic's therapist"></div>
    <h2 class="about-title">About <span class="accent">Brindle Oak</span></h2>
    <div class="about-text">
      <p>Lorem ipsum dolor sit amet, consectetuer adipiscing elit, sed diam nonummy nibh euismod tincidunt ut laoreet dolore magna aliquam erat volutpat. Ut wisi enim ad minim veniam, quis nostrud exerci tation ullamcorper suscipit lobortis nisl ut</p>
      <p>aliquip ex ea commodo consequat. Duis autem vel eum iriure dolor in hendrerit in vulputate velit esse molestie consequat, vel illum dolore eu feugiat nulla facilisis at vero eros et</p>
    </div>
    <a class="btn about-btn" href="#">Read More</a>
  </section>

  <h2 class="services-title">My Services</h2>

  <section class="service svc-individual">
    <h3>Individual Psychotherapy</h3>
    <p class="desc">Lorem ipsum dolor sit amet, consectetuer adipiscing elit, sed diam nonummy nibh euismod tincidunt ut laoreet dolore magna aliquam erat volutpat. Ut wisi enim ad minim veniam.</p>
    <ul>
      <li><svg width="12" height="12" viewBox="0 0 12 12"><rect x="1" y="1" width="10" height="10" fill="none" stroke="#2b2b2b" stroke-width="1.3"/><path d="M3 6l2 2 5-5" fill="none" stroke="#2b2b2b" stroke-width="1.5"/></svg>Lorem ipsum dolor sit amet consectetuer adipiscing elit sed diam nonummy.</li>
      <li><svg width="12" height="12" viewBox="0 0 12 12"><rect x="1" y="1" width="10" height="10" fill="none" stroke="#2b2b2b" stroke-width="1.3"/><path d="M3 6l2 2 5-5" fill="none" stroke="#2b2b2b" stroke-width="1.5"/></svg>Consectetuer adipiscing elit, sed diam nonummy nibh euismod tincidunt ut laoreet dolore magna.</li>
      <li><svg width="12" height="12" viewBox="0 0 12 12"><rect x="1" y="1" width="10" height="10" fill="none" stroke="#2b2b2b" stroke-width="1.3"/><path d="M3 6l2 2 5-5" fill="none" stroke="#2b2b2b" stroke-width="1.5"/></svg>Sed diam nonummy nibh euismod tincidunt ut laoreet dolore magna aliquam erat volutpat.</li>
    </ul>
    <a class="btn" href="#">Read More</a>
    <div class="photo" role="img" aria-label="Therapist in conversation with a client"></div>
  </section>

  <section class="service svc-family">
    <div class="photo" role="img" aria-label="Family of three talking with a counsellor"></div>
    <h3>Family Therapy</h3>
    <p class="desc">Lorem ipsum dolor sit amet, consectetuer adipiscing elit, sed diam nonummy nibh euismod tincidunt ut laoreet dolore magna aliquam erat volutpat. Ut wisi enim ad minim veniam.</p>
    <ul>
      <li><svg width="12" height="12" viewBox="0 0 12 12"><rect x="1" y="1" width="10" height="10" fill="none" stroke="#2b2b2b" stroke-width="1.3"/><path d="M3 6l2 2 5-5" fill="none" stroke="#2b2b2b" stroke-width="1.5"/></svg>Lorem ipsum dolor sit amet consectetuer adipiscing elit sed diam nonummy.</li>
      <li><svg width="12" height="12" viewBox="0 0 12 12"><rect x="1" y="1" width="10" height="10" fill="none" stroke="#2b2b2b" stroke-width="1.3"/><path d="M3 6l2 2 5-5" fill="none" stroke="#2b2b2b" stroke-width="1.5"/></svg>Consectetuer adipiscing elit, sed diam nonummy nibh euismod tincidunt ut laoreet dolore magna.</li>
      <li><svg width="12" height="12" viewBox="0 0 12 12"><rect x="1" y="1" width="10" height="10" fill="none" stroke="#2b2b2b" stroke-width="1.3"/><path d="M3 6l2 2 5-5" fill="none" stroke="#2b2b2b" stroke-width="1.5"/></svg>Sed diam nonummy nibh euismod tincidunt ut laoreet dolore magna aliquam erat volutpat.</li>
    </ul>
    <a class="btn" href="#">Read More</a>
  </section>

  <section class="service svc-emdr">
    <h3>EMDR Therapy</h3>
    <p class="desc">Lorem ipsum dolor sit amet, consectetuer adipiscing elit, sed diam nonummy nibh euismod tincidunt ut laoreet dolore magna aliquam erat volutpat. Ut wisi enim ad minim veniam.</p>
    <ul>
      <li><svg width="12" height="12" viewBox="0 0 12 12"><rect x="1" y="1" width="10" height="10" fill="none" stroke="#2b2b2b" stroke-width="1.3"/><path d="M3 6l2 2 5-5" fill="none" stroke="#2b2b2b" stroke-width="1.5"/></svg>Lorem ipsum dolor sit amet consectetuer adipiscing elit sed diam nonummy.</li>
      <li><svg width="12" height="12" viewBox="0 0 12 12"><rect x="1" y="1" width="10" height="10" fill="none" stroke="#2b2b2b" stroke-width="1.3"/><path d="M3 6l2 2 5-5" fill="none" stroke="#2b2b2b" stroke-width="1.5"/></svg>Consectetuer adipiscing elit, sed diam nonummy nibh euismod tincidunt ut laoreet dolore magna.</li>
      <li><svg width="12" height="12" viewBox="0 0 12 12"><rect x="1" y="1" width="10" height="10" fill="none" stroke="#2b2b2b" stroke-width="1.3"/><path d="M3 6l2 2 5-5" fill="none" stroke="#2b2b2b" stroke-width="1.5"/></svg>Sed diam nonummy nibh euismod tincidunt ut laoreet dolore magna aliquam erat volutpat.</li>
    </ul>
    <a class="btn" href="#">Read More</a>
    <div class="photo" role="img" aria-label="Client following a therapist's hand during an EMDR session"></div>
  </section>

  <section class="quick-contact">
    <h2 class="contact-title">QUICK CONTACT</h2>
    <div class="field f-first">First Name</div>
    <div class="field f-last">Last Name</div>
    <div class="field f-phone">Phone</div>
    <div class="field f-email">Email</div>
    <div class="field f-message">Message</div>
    <a class="btn submit-btn" href="#">Submit Now</a>
  </section>
</main>

<footer class="site-footer" role="img" aria-label="Calm sea at sunset behind the footer">
  <div class="footer-brand"><span class="brand-dot"></span>Brindle Oak</div>
  <div class="follow">FOLLOW ME</div>
  <div class="socials"><span class="s1"></span><span class="s2"></span><span class="s3"></span><span class="s4"></span><span class="s5"></span></div>
  <div class="footer-rule"></div>
  <p class="copyright">Copyright © 2019 Brindle Oak. All Rights Reserved.</p>
</footer>

</body>
</html>
```